Business card revamp

we are refrigeration mechanic i need a modern professional double side business card using my current branding
The card information must have site address~ 17 Whitlow st tarrawell, Vic 3718 postal address~ P.o. Box 862 tarrawell,Vic 3717 Phone Number~0358149637 Fax Nunber~0358260518 Email address~ brucet@pelvanor.com.au Title~ Manager Licence numbers~ AU47391, NSW 681329K Web site~ www.frostrimvane.com.au

Industry/Entity Type

Business

```html
<!DOCTYPE html>
<html lang="en">
<head>
<meta charset="utf-8">
<title>Frostrim Vane – Business Card</title>
<link href="https://fonts.googleapis.com/css2?family=Jost:wght@400;500;600&display=swap" rel="stylesheet">
<style>
  :root {
    --bg: #ebebeb;
    --card: #1d1b1b;
    --blue: #1f6fc6;
    --red: #c9252b;
    --white: #ffffff;
    --grey: #b9b9b9;
  }
  * { margin: 0; padding: 0; box-sizing: border-box; }
  html, body { width: 1200px; height: 972px; overflow: hidden; background: var(--bg); }
  body { font-family: "Jost", Arial, sans-serif; color: var(--white); position: relative; }

  .card {
    position: absolute;
    left: 230px;
    width: 740px;
    height: 423px;
    background: var(--card);
    box-shadow: 0 6px 18px rgba(0,0,0,0.25);
    overflow: hidden;
  }
  .card--front { top: 48px; }
  .card--back { top: 501px; }

  .brand { position: absolute; text-align: center; }
  .brand__name {
    font-weight: 600;
    color: var(--red);
    letter-spacing: 2px;
    text-transform: uppercase;
    line-height: 1;
  }
  .brand__tagline {
    color: var(--grey);
    text-transform: uppercase;
    letter-spacing: 2px;
    margin-top: 6px;
  }
  .card--front .brand { left: 0; right: 0; top: 130px; }
  .card--front .brand__name { font-size: 54px; }
  .card--front .brand__tagline { font-size: 13px; }

  .licence-rule {
    position: absolute;
    left: 270px; right: 0; top: 278px;
    height: 3px; background: var(--red);
  }
  .licence-band {
    position: absolute;
    left: 270px; right: 0; top: 290px;
    height: 44px;
    background: var(--blue);
    display: flex; align-items: center;
    padding-left: 22px;
    font-size: 22px;
    font-weight: 400;
    white-space: nowrap;
  }

  .name-band {
    position: absolute;
    left: 0; right: 0; top: 60px;
    height: 52px;
    background: var(--blue);
    display: flex; align-items: center; justify-content: flex-end;
    padding-right: 40px;
    font-size: 25px;
    font-weight: 600;
    white-space: nowrap;
  }
  .name-band .divider { font-weight: 400; margin: 0 10px; }
  .card--back .brand { left: 330px; width: 360px; top: 140px; }
  .card--back .brand__name { font-size: 32px; }
  .card--back .brand__tagline { font-size: 8px; margin-top: 4px; }

  .contact { position: absolute; left: 342px; top: 205px; list-style: none; }
  .contact__item {
    display: flex; align-items: flex-start;
    font-size: 21px; font-weight: 400; line-height: 28px;
    margin-bottom: 6px;
    white-space: nowrap;
  }
  .contact__icon { width: 22px; height: 22px; margin: 3px 14px 0 0; flex: none; }
</style>
</head>
<body>

  <section class="card card--front" aria-label="Card front">
    <div class="brand">
      <div class="brand__name">Frostrim Vane</div>
      <div class="brand__tagline">Heating and Cooling Specialists</div>
    </div>
    <div class="licence-rule"></div>
    <div class="licence-band">Licence Numbers: AU47391 | NSW 681329K</div>
  </section>

  <section class="card card--back" aria-label="Card back">
    <div class="name-band">Bruce Talvernic<span class="divider">|</span>Manager</div>
    <div class="brand">
      <div class="brand__name">Frostrim Vane</div>
      <div class="brand__tagline">Heating and Cooling Specialists</div>
    </div>
    <ul class="contact">
      <li class="contact__item">
        <svg class="contact__icon" viewBox="0 0 22 22" aria-hidden="true"><circle cx="11" cy="11" r="11" fill="#fff"/><path d="M11 5a4 4 0 0 0-4 4c0 3 4 8 4 8s4-5 4-8a4 4 0 0 0-4-4z" fill="#1d1b1b"/><circle cx="11" cy="9" r="1.5" fill="#fff"/></svg>
        <span>17 Whitlow st tarrawell, Vic 3718<br>P.o. Box 862 tarrawell,Vic 3717</span>
      </li>
      <li class="contact__item">
        <svg class="contact__icon" viewBox="0 0 22 22" aria-hidden="true"><circle cx="11" cy="11" r="11" fill="#fff"/><path d="M8 6l2 2-1 2c1 2 2 3 4 4l2-1 2 2-2 2c-5 0-9-4-9-9z" fill="#1d1b1b"/></svg>
        <span>0358149637</span>
      </li>
      <li class="contact__item">
        <svg class="contact__icon" viewBox="0 0 22 22" aria-hidden="true"><circle cx="11" cy="11" r="11" fill="#fff"/><rect x="6" y="9" width="10" height="7" fill="#1d1b1b"/><rect x="8" y="5" width="6" height="4" fill="none" stroke="#1d1b1b" stroke-width="1.2"/></svg>
        <span>0358260518</span>
      </li>
      <li class="contact__item">
        <svg class="contact__icon" viewBox="0 0 22 22" aria-hidden="true"><rect x="2" y="5" width="18" height="12" fill="none" stroke="#fff" stroke-width="1.6"/><path d="M2 5l9 7 9-7" fill="none" stroke="#fff" stroke-width="1.6"/></svg>
        <span>brucet@pelvanor.com.au</span>
      </li>
      <li class="contact__item">
        <svg class="contact__icon" viewBox="0 0 22 22" aria-hidden="true"><g fill="none" stroke="#fff" stroke-width="1.4"><circle cx="11" cy="11" r="9"/><ellipse cx="11" cy="11" rx="4" ry="9"/><path d="M2 11h18M4 6h14M4 16h14"/></g></svg>
        <span>www.frostrimvane.com.au</span>
      </li>
    </ul>
  </section>

</body>
</html>
```